KO-TRA , Artificial hedge flyer

i need new flyer, in att i'm sending old one but as we produce artificial flowers, trees and most popular is artificial green hedge, and it's used from variety places, from swimming pool, restaurants, bars, private terrace, gardens, to protect from neighbor :-) . from beginning is all our product, it's not imported from other producer. we are doing it by measure what we get from customer ( tailor made ) , we give guaranty 15-20 years on all weather that will not loos color, etc.. you can see some pictures in att on old flyer, and some new pictures of same in space newly added. we'd like more pictures with samples of use, etc.you can see our product on www.ko-tra.hr so you can closely known what we are producing, and what for we need new flyer. we have plenty of new picture that are not on our web, so i can use it for new flyer.

Font styles to use
Sans Serif

Requirements
Must have
• company logo, contact info ( sent in word document in att ), logo of croatian product ( on old flyer in att on front side), stamp Quality since 1950 if you could change year to 1960, last time they made mistake and write 1950 ),
Nice to have
• flyer 3 fold type, or if you think it will look better only double side flyer, depend of design and theme so everyone can understand what is our business

```html
<!DOCTYPE html>
<html lang="hr">
<head>
<meta charset="utf-8">
<title>KO-TRA – flyer</title>
<link rel="stylesheet" href="https://fonts.googleapis.com/css2?family=Montserrat:wght@400;600;700;800&family=Oswald:wght@300;400;500&display=swap">
<style>
:root{
  --page:#e3e4e1;
  --hedge-dark:#1f3a1c;
  --hedge:#3d6028;
  --leaf:#5bab48;
  --leaf-bright:#2bb34a;
  --mint:#a6e0bd;
  --logo:#7fcf6a;
  --swoosh:#b9bbb4;
  --charcoal:#3a3c3b;
  --charcoal-deep:#2c2e2d;
  --ink:#2a2a2a;
  --white:#ffffff;
  --muted:#c9cbc6;
}
*{margin:0;padding:0;box-sizing:border-box}
html,body{width:1200px;height:2713px;overflow:hidden;background:var(--page)}
body{position:relative;font-family:"Montserrat",sans-serif;color:var(--white)}
.sheet{position:absolute;overflow:hidden;box-shadow:0 4px 14px rgba(0,0,0,.25)}
.sheet svg.art{position:absolute;inset:0}
.abs{position:absolute}
.front{left:60px;top:160px;width:1028px;height:790px}
.back{left:58px;top:1785px;width:1024px;height:727px}

.brand{display:flex;align-items:center;gap:12px;font-family:"Montserrat",sans-serif;font-weight:600;color:var(--logo);letter-spacing:1px}
.brand .dot{border-radius:50%;background:var(--logo)}
.front .brand{left:62px;top:48px;font-size:50px}
.front .brand .dot{width:44px;height:44px}

.heading{font-family:"Montserrat",sans-serif;font-weight:800;display:flex;align-items:center;gap:8px}
.heading .mark{width:18px;height:18px;border-radius:50%;background:var(--white)}
.about-title{left:78px;top:150px;font-size:36px}
.about-text{left:84px;top:205px;width:430px;font-size:11.4px;line-height:16.6px;text-shadow:0 1px 2px rgba(0,0,0,.6)}
.offer-title{left:418px;top:392px;font-size:36px}

.offer-list{left:405px;top:448px;width:620px;font-family:"Oswald",sans-serif;font-weight:300;font-size:15px;letter-spacing:-.2px}
.offer-list ul{list-style:none;display:flex;gap:14px;height:36px;align-items:center}
.offer-list ul.second{padding-left:22px}
.offer-list li{display:flex;align-items:center;gap:5px;white-space:nowrap}
.offer-list li::before{content:"";width:10px;height:10px;border-radius:50%;background:var(--white)}

.badge-square{left:680px;top:590px;width:28px;height:28px;background:var(--white);opacity:.85}
.badge-circle{left:762px;top:578px;width:54px;height:54px;border-radius:50%;border:2px solid var(--white);opacity:.85}

.front .web{left:572px;top:667px;font-size:36px;font-weight:800;letter-spacing:1px}
.contact-row{left:500px;top:720px;display:flex;align-items:flex-end;gap:22px;font-family:"Oswald",sans-serif;font-size:14px;line-height:18px}
.contact-row .item{display:flex;align-items:center;gap:10px}
.contact-row small{display:block;font-size:10.5px;color:var(--muted)}
.icon{fill:var(--white)}

.back .brand{left:0;right:0;top:58px;justify-content:center;font-size:58px}
.back .brand .dot{width:52px;height:52px}
.card-text{text-align:center}
.card-title{font-family:"Oswald",sans-serif;font-weight:500;font-size:25px;margin-bottom:10px}
.card-body{font-family:"Oswald",sans-serif;font-weight:300;font-size:14px;line-height:20.5px}
.quality{left:40px;top:355px;width:230px;color:var(--ink)}
.offer{left:385px;top:410px;width:250px}
.offer .card-body{font-family:"Montserrat",sans-serif;font-weight:400;font-size:12.5px;line-height:16.6px}
.seat{left:745px;top:355px;width:255px;color:var(--ink)}
.seat .card-body{font-size:16px;line-height:22px}
.seat .pin{margin:16px auto 4px;display:block}
.seat .addr{font-size:15px;line-height:19px}

.foot{text-align:center}
.foot p{font-family:"Montserrat",sans-serif;font-size:10px;margin-bottom:8px}
.foot-phone{left:22px;top:635px;width:268px}
.foot-phone .nums{display:flex;align-items:center;justify-content:center;gap:10px;font-weight:700;font-size:17px;line-height:20px;text-align:left}
.foot-web{left:332px;top:610px;width:364px}
.foot-web p{font-size:12px;line-height:16px;margin:16px 0 14px}
.foot-web .web{font-size:32px;font-weight:800;letter-spacing:1px}
.foot-mail{left:714px;top:635px;width:288px}
.foot-mail .mail{display:flex;align-items:center;justify-content:center;gap:14px;font-size:17px;margin-top:14px}
</style>
</head>
<body>

<section class="sheet front" aria-label="Prednja strana letka">
  <svg class="art" width="1028" height="790" viewBox="0 0 1028 790">
    <defs>
      <linearGradient id="hedgeG" x1="0" y1="0" x2="1" y2="1">
        <stop offset="0" stop-color="#466b2c"/><stop offset=".6" stop-color="#365624"/><stop offset="1" stop-color="#27401c"/>
      </linearGradient>
      <linearGradient id="terraceG" x1="0" y1="0" x2="0" y2="1">
        <stop offset="0" stop-color="#b9c6c9"/><stop offset=".28" stop-color="#7e9aa6"/><stop offset=".42" stop-color="#4f6b3a"/><stop offset=".65" stop-color="#8a4d2e"/><stop offset="1" stop-color="#5a5f57"/>
      </linearGradient>
      <linearGradient id="flowersG" x1="0" y1="0" x2="1" y2="1">
        <stop offset="0" stop-color="#6a7d55"/><stop offset=".4" stop-color="#8c6a7e"/><stop offset=".7" stop-color="#9b8a6b"/><stop offset="1" stop-color="#4a3f33"/>
      </linearGradient>
      <linearGradient id="cafeG" x1="0" y1="0" x2="1" y2="1">
        <stop offset="0" stop-color="#4a4c4a"/><stop offset="1" stop-color="#2c2e2d"/>
      </linearGradient>
      <radialGradient id="poolG" cx=".5" cy=".6" r=".6">
        <stop offset="0" stop-color="#3f83c6"/><stop offset=".5" stop-color="#5f8a4a"/><stop offset="1" stop-color="#b87355"/>
      </radialGradient>
    </defs>
    <rect width="1028" height="790" fill="url(#hedgeG)" role="img" aria-label="Zid od umjetne živice"/>
    <path d="M520 0 L1028 0 L1028 430 L800 430 C700 310 610 160 520 0 Z" fill="url(#terraceG)" role="img" aria-label="Drvena terasa uz more obrubljena umjetnom živicom"/>
    <path d="M520 0 C610 160 700 310 800 430" fill="none" stroke="var(--swoosh)" stroke-width="26" opacity=".85"/>
    <path d="M0 385 C150 370 300 520 380 790 L0 790 Z" fill="url(#flowersG)" role="img" aria-label="Vertikalni vrt s cvijećem i pleteni stolci"/>
    <path d="M0 380 C170 350 320 520 395 790" fill="none" stroke="var(--swoosh)" stroke-width="18" opacity=".7"/>
    <path d="M390 790 C430 650 520 560 640 542 L1028 542 L1028 790 Z" fill="url(#cafeG)" role="img" aria-label="Kafić terasa sa stolicama"/>
    <path d="M380 790 C420 645 515 552 640 532" fill="none" stroke="var(--swoosh)" stroke-width="16" opacity=".85"/>
    <rect x="400" y="442" width="628" height="94" fill="var(--leaf)" opacity=".93"/>
    <circle cx="280" cy="490" r="122" fill="var(--swoosh)"/>
    <circle cx="280" cy="490" r="108" fill="url(#poolG)" role="img" aria-label="Bazen s ležaljkom uz umjetnu živicu"/>
  </svg>

  <div class="abs brand"><span class="dot"></span>KO-TRA d.o.o.</div>

  <h2 class="abs heading about-title"><span class="mark"></span>O nama</h2>
  <p class="abs about-text">KO-TRA d.o.o. osnovana je 1992 godine i nastavlja obiteljsku tradiciju započetu davne 1950. Bavimo se proizvodnjom umjetne živice, drveća, dekorativnog zelenila, umjetnog cvijeća i aranžmana za razne prigode (ukrasni buketi, cvjetni stupići, cvjetnih kugli, grobnih aranžmana i sl.), kao, umjetnih latica u svim bojama i dezenima, bonsaia, žardinjera po narudžbi Vanjsko i unutranje uređenje poslovnih i trgovačkih centara, ugostiteljskih, stambenih i sportskih objekata, izrada scena za film i kazalište, wellness centri , bazeni, hoteli.</p>

  <h2 class="abs heading offer-title"><span class="mark"></span>Nudimo</h2>
  <div class="abs offer-list">
    <ul><li>VANJSKO I UNUTRANJE</li><li>IZRADA SCENA ZA FILM I KAZALIŠTE</li><li>STAMBENIH I SPORTSKIH OBJEKATA</li></ul>
    <ul class="second"><li>UREĐENJE POSLOVNIH ITRGOVAČKIH CENTARA</li><li>WELLNESS CENTRI</li><li>BAZENI</li><li>HOTELI</li></ul>
  </div>

  <div class="abs badge-square" aria-label="Oznaka domaćeg proizvoda"></div>
  <div class="abs badge-circle" aria-label="Pečat kvalitete"></div>

  <div class="abs web">www.ko-tra.hr</div>

  <div class="abs contact-row">
    <div class="item">
      <svg width="20" height="28" viewBox="0 0 20 28"><path class="icon" d="M10 0C4.5 0 0 4.4 0 9.8 0 17 10 28 10 28s10-11 10-18.2C20 4.4 15.5 0 10 0zm0 14a4.2 4.2 0 1 1 0-8.4 4.2 4.2 0 0 1 0 8.4z"/></svg>
      <div><small>Prodajno-izložbeni Salon</small>Vrtna cesta 24, LUGOVI<br>10437 Sv.Klara</div>
    </div>
    <div class="item">
      <svg width="28" height="28" viewBox="0 0 24 24"><path class="icon" d="M6.6 10.8a15 15 0 0 0 6.6 6.6l2.2-2.2c.3-.3.7-.4 1-.2 1.1.4 2.3.6 3.6.6.6 0 1 .4 1 1V20c0 .6-.4 1-1 1A17 17 0 0 1 3 4c0-.6.4-1 1-1h3.5c.6 0 1 .4 1 1 0 1.3.2 2.5.6 3.6.1.3 0 .7-.2 1z"/></svg>
      <div>+385 91 555 0140<br>+385 99 555 0182</div>
    </div>
    <div class="item">
      <svg width="20" height="15" viewBox="0 0 20 15"><path class="icon" d="M0 0h20v2L10 8 0 2zM0 4l10 6 10-6v11H0z"/></svg>
      <div>info@ko-tra.hr</div>
    </div>
  </div>
</section>

<section class="sheet back" aria-label="Stražnja strana letka">
  <svg class="art" width="1024" height="727" viewBox="0 0 1024 727">
    <defs>
      <linearGradient id="lotG" x1="0" y1="0" x2="0" y2="1">
        <stop offset="0" stop-color="#2b4a24"/><stop offset=".32" stop-color="#c8ccd0"/><stop offset=".5" stop-color="#8e9598"/><stop offset=".7" stop-color="#3e5e2c"/><stop offset="1" stop-color="#6b6d68"/>
      </linearGradient>
      <radialGradient id="circG" cx=".5" cy=".5" r=".6">
        <stop offset="0" stop-color="#5d8f3b"/><stop offset="1" stop-color="#2d4d22"/>
      </radialGradient>
      <radialGradient id="shopG" cx=".5" cy=".5" r=".6">
        <stop offset="0" stop-color="#4f8a3a"/><stop offset=".6" stop-color="#7a4a45"/><stop offset="1" stop-color="#2a2c2b"/>
      </radialGradient>
      <radialGradient id="gazeboG" cx=".5" cy=".4" r=".6">
        <stop offset="0" stop-color="#c99c5c"/><stop offset=".55" stop-color="#5b8a3a"/><stop offset="1" stop-color="#3a6a2a"/>
      </radialGradient>
    </defs>
    <rect width="1024" height="727" fill="url(#lotG)" role="img" aria-label="Parkiralište ispred salona s umjetnom živicom i vrtnim namještajem"/>
    <path d="M0 0 L1024 0 L1024 225 C820 250 660 235 512 240 C360 235 200 250 0 225 Z" fill="var(--hedge-dark)"/>
    <path d="M0 0 L170 0 C100 60 40 110 0 130 Z" fill="var(--mint)"/>
    <path d="M1024 0 L850 0 C920 60 980 110 1024 130 Z" fill="var(--mint)"/>
    <path d="M0 225 L0 290 L40 270" fill="var(--mint)" opacity=".9"/>
    <path d="M1024 225 L1024 290 L984 270" fill="var(--mint)" opacity=".9"/>
    <rect x="40" y="215" width="230" height="420" fill="var(--white)" opacity=".82"/>
    <circle cx="155" cy="215" r="95" fill="var(--white)" opacity=".82"/>
    <circle cx="155" cy="215" r="82" fill="url(#circG)" role="img" aria-label="Unutarnji prostor uređen umjetnom živicom"/>
    <rect x="385" y="235" width="250" height="375" fill="var(--charcoal-deep)" opacity=".78"/>
    <circle cx="510" cy="230" r="90" fill="var(--charcoal-deep)"/>
    <circle cx="510" cy="230" r="80" fill="url(#shopG)" role="img" aria-label="Umjetno drveće i cvjetni aranžmani"/>
    <rect x="745" y="215" width="255" height="420" fill="var(--white)" opacity=".82"/>
    <circle cx="872" cy="215" r="100" fill="var(--white)" opacity=".82"/>
    <circle cx="872" cy="215" r="86" fill="url(#gazeboG)" role="img" aria-label="Drvena sjenica s umjetnom živicom"/>
    <path d="M22 727 L22 650 Q22 632 40 632 L272 632 Q290 632 290 650 L290 727 Z" fill="var(--charcoal)"/>
    <path d="M332 727 L332 625 Q332 607 350 607 L678 607 Q696 607 696 625 L696 727 Z" fill="var(--leaf-bright)"/>
    <path d="M714 727 L714 650 Q714 632 732 632 L984 632 Q1002 632 1002 650 L1002 727 Z" fill="var(--charcoal)"/>
  </svg>

  <div class="abs brand"><span class="dot"></span>KO-TRA d.o.o.</div>

  <div class="abs card-text quality">
    <h3 class="card-title">Kvalitetan rad</h3>
    <p class="card-body">Pazimo na svaki detalj i koristimo<br>prvoklasne proizvode kako bismo<br>postigli potpuno izvrstan i<br>profesionalan izgled, tako da naše<br>ukrasno zelenilo i umjetni<br>aranžmani stvaraju potpuno<br>ugodne prostore s velikim<br>utjecajem za vaše poslovanje.</p>
  </div>

  <div class="abs card-text offer">
    <h3 class="card-title">Naša ponuda</h3>
    <p class="card-body">Unutarnje i vanjsko uređenje<br>poslovnih, stambenih,<br>sportskih i ostalih prostora<br>umjetnom živicom,<br>dekorativnim zelenilom i<br>cvijećem, drvećem i<br>aranžmanima</p>
  </div>

  <div class="abs card-text seat">
    <h3 class="card-title">Naše sjedište</h3>
    <p class="card-body">Posjetite naše sjedište<br>i pažljivije pogledajte<br>naše proizvode</p>
    <svg class="pin" width="22" height="30" viewBox="0 0 20 28"><path fill="var(--ink)" d="M10 0C4.5 0 0 4.4 0 9.8 0 17 10 28 10 28s10-11 10-18.2C20 4.4 15.5 0 10 0zm0 14a4.2 4.2 0 1 1 0-8.4 4.2 4.2 0 0 1 0 8.4z"/></svg>
    <p class="card-body addr">Vrtna cesta 24, LUGOVI<br>10437 Sv.Klara</p>
  </div>

  <div class="abs foot foot-phone">
    <p>Nazovite, raspitajte se ili dogovorite sastanak već danas!</p>
    <div class="nums">
      <svg width="30" height="30" viewBox="0 0 24 24"><path class="icon" d="M6.6 10.8a15 15 0 0 0 6.6 6.6l2.2-2.2c.3-.3.7-.4 1-.2 1.1.4 2.3.6 3.6.6.6 0 1 .4 1 1V20c0 .6-.4 1-1 1A17 17 0 0 1 3 4c0-.6.4-1 1-1h3.5c.6 0 1 .4 1 1 0 1.3.2 2.5.6 3.6.1.3 0 .7-.2 1z"/></svg>
      <span>+385 91 555 0140<br>+385 99 555 0182</span>
    </div>
  </div>

  <div class="abs foot foot-web">
    <p>Posjetite galeriju fotografija na našoj web<br>stranici i pogledajte kvalitetu naših gotovih radova.</p>
    <div class="web">www.ko-tra.hr</div>
  </div>

  <div class="abs foot foot-mail">
    <p>Pišite nam i stupit ćemo u kontakt s vama</p>
    <div class="mail">
      <svg width="28" height="21" viewBox="0 0 20 15"><path class="icon" d="M0 0h20v2L10 8 0 2zM0 4l10 6 10-6v11H0z"/></svg>
      <span>info@ko-tra.hr</span>
    </div>
  </div>
</section>

</body>
</html>
```